Communications & Broadcast Consulting/PR/Media Relations & Public Affairs

My main goals are to provide communications support to school districts, small towns/cities/hospitals and private businesses in the form of press releases, media relations, public affairs. I also have 25 years experience as a television news anchor/reporter and I'm open to free-lance reporting in both Indianapolis and other markets. My specialty is working with the media.
Communications

```html
<!DOCTYPE html>
<html lang="en">
<head>
<meta charset="utf-8">
<title>Brightwell Communications – Business Card</title>
<link href="https://fonts.googleapis.com/css2?family=Open+Sans:wght@400;600&display=swap" rel="stylesheet">
<style>
  :root {
    --page: #e9eaea;
    --card-white: #ffffff;
    --ink: #1b1b1b;
    --panel-black: #1a1a1a;
    --brand-green: #1fae4b;
    --light-green: #5cc46d;
    --text-grey: #333333;
  }
  * { box-sizing: border-box; margin: 0; padding: 0; }
  html, body { width: 1200px; height: 676px; overflow: hidden; }
  body {
    background: var(--page);
    font-family: "Open Sans", Arial, sans-serif;
    position: relative;
  }
  .card {
    position: absolute;
    top: 201px;
    width: 480px;
    height: 274px;
    background: var(--card-white);
    box-shadow: 0 6px 18px rgba(0,0,0,0.18);
    overflow: hidden;
  }

  /* Front */
  .card--front { left: 80px; }
  .front__panel {
    position: absolute;
    top: 0; right: 0;
    width: 52%;
    height: 100%;
    background: var(--panel-black);
  }
  .front__brand {
    position: absolute;
    left: 26px;
    top: 104px;
    display: flex;
    align-items: center;
    gap: 10px;
  }
  .brand-dot {
    width: 14px; height: 14px;
    border-radius: 50%;
    background: var(--brand-green);
    flex: none;
  }
  .brand-name {
    font-weight: 400;
    color: var(--ink);
    line-height: 1.15;
  }
  .front__brand .brand-name { font-size: 19px; }

  /* Back */
  .card--back { left: 640px; }
  .back__brand {
    position: absolute;
    right: 22px;
    top: 44px;
    display: flex;
    align-items: center;
    gap: 8px;
  }
  .back__brand .brand-name { font-size: 15px; text-align: right; }
  .name-band {
    position: absolute;
    left: 0; right: 0;
    top: 104px;
    height: 28px;
    background: var(--brand-green);
    display: flex;
    align-items: center;
    padding-left: 22px;
    color: #fff;
  }
  .name-band__name { font-size: 15px; }
  .name-band__sep {
    margin: 0 9px;
    width: 1px; height: 18px;
    background: rgba(255,255,255,0.8);
  }
  .name-band__role { font-size: 10.5px; }
  .contact-list {
    position: absolute;
    left: 20px;
    top: 138px;
    list-style: none;
    font-size: 10.5px;
    color: var(--text-grey);
    line-height: 1.55;
    z-index: 1;
  }
  .contact-list li { display: flex; align-items: center; gap: 7px; }
  .contact-list svg { width: 9px; height: 9px; flex: none; }
  .address {
    position: absolute;
    right: 22px;
    top: 176px;
    display: flex;
    align-items: center;
    gap: 5px;
    font-size: 10.5px;
    color: var(--text-grey);
    z-index: 1;
  }
  .address svg { width: 9px; height: 12px; }
  .back__swoosh {
    position: absolute;
    left: 0; bottom: 0;
    width: 480px;
    height: 80px;
  }
</style>
</head>
<body>

  <section class="card card--front" aria-label="Card front">
    <div class="front__brand">
      <span class="brand-dot"></span>
      <span class="brand-name">Brightwell<br>Communications</span>
    </div>
    <div class="front__panel"></div>
  </section>

  <section class="card card--back" aria-label="Card back">
    <svg class="back__swoosh" viewBox="0 0 480 80" preserveAspectRatio="none" aria-hidden="true">
      <path d="M0 10 C100 0 200 30 270 52 C340 74 420 78 480 64 L480 80 L0 80 Z" fill="var(--panel-black)"/>
      <path d="M0 18 C100 10 200 40 268 60 C340 80 420 82 480 70 L480 75 C420 86 340 84 266 66 C198 46 100 18 0 24 Z" fill="var(--light-green)"/>
      <path d="M0 27 C100 22 200 50 266 70 C330 86 420 88 480 79 L480 80 L0 80 Z" fill="var(--panel-black)"/>
    </svg>

    <div class="back__brand">
      <span class="brand-dot"></span>
      <span class="brand-name">Brightwell<br>Communications</span>
    </div>

    <div class="name-band">
      <span class="name-band__name">your name</span>
      <span class="name-band__sep"></span>
      <span class="name-band__role">designation</span>
    </div>

    <ul class="contact-list">
      <li>
        <svg viewBox="0 0 10 10" aria-hidden="true"><rect x="1" y="1" width="8" height="8" rx="1" fill="var(--text-grey)"/><rect x="3" y="3" width="4" height="2" fill="#fff"/></svg>
        IN 46099 317.555.0142
      </li>
      <li>
        <svg viewBox="0 0 10 10" aria-hidden="true"><rect x="2.5" y="0.5" width="5" height="9" rx="1" fill="none" stroke="var(--text-grey)"/></svg>
        317.555.0187
      </li>
      <li>
        <svg viewBox="0 0 10 10" aria-hidden="true"><rect x="0.5" y="2" width="9" height="6" fill="var(--text-grey)"/><path d="M0.5 2 L5 5.5 L9.5 2" fill="none" stroke="#fff"/></svg>
        jbrightwell77@mailbox.com
      </li>
    </ul>

    <div class="address">
      <span>2180 Marlow Lane Indianapolis</span>
      <svg viewBox="0 0 10 13" aria-hidden="true"><path d="M5 12.5 C2 8 1 6.5 1 4.5 A4 4 0 0 1 9 4.5 C9 6.5 8 8 5 12.5 Z" fill="var(--text-grey)"/><circle cx="5" cy="4.5" r="1.5" fill="#fff"/></svg>
    </div>
  </section>

</body>
</html>
```